Builder of high-end, expensive tables and other furniture

Build a website that represents what we do. I want a luxury feel that appeals to those who can afford our products. We build very high end tables and other furniture using trees that have fallen or are standing dead. We never cut living trees. Trees are harvested, milled, and kiln dried. Then that lumber is meticulously turned into fine furniture using the best equipment. Our furniture prices range from $1,000-$20,000.

Trying to figure out how to raise my spend.

```html
<!DOCTYPE html>
<html lang="en">
<head>
<meta charset="utf-8">
<title>Heartwood Tables — Sustainable Luxury Furniture</title>
<link href="https://fonts.googleapis.com/css2?family=Belleza&family=Urbanist:wght@400;500;600&display=swap" rel="stylesheet">
<style>
:root{
  --bg:#0e1117;
  --bg-deep:#0b0d12;
  --panel:#1a1c21;
  --panel-2:#15171c;
  --text:#ffffff;
  --muted:#b9bcc3;
  --orange:#f0692c;
  --orange-soft:#f59a63;
  --blue:#3a86d8;
  --line:#2a2d33;
}
*{margin:0;padding:0;box-sizing:border-box}
html,body{width:1200px;height:3656px;overflow:hidden}
body{background:var(--bg);color:var(--text);font-family:'Urbanist',sans-serif;position:relative}
.abs{position:absolute}
.display{font-family:'Belleza',sans-serif;font-weight:400}
.eyebrow{font-size:15px;color:var(--blue);letter-spacing:.3px;text-transform:uppercase}
.btn{position:absolute;display:flex;align-items:center;justify-content:center;font-family:'Belleza',sans-serif;font-size:19px;color:#fff;border-radius:5px}
.btn-fill{background:linear-gradient(90deg,var(--orange),var(--orange-soft))}
.btn-line{border:1.5px solid #fff}
.brand{font-family:'Belleza',sans-serif;font-size:34px;color:var(--orange);display:flex;align-items:center;gap:10px}
.brand .dot{width:14px;height:14px;border-radius:50%;background:var(--orange)}

/* header & hero */
.hero-bg{left:0;top:0;width:1200px;height:617px;background:radial-gradient(ellipse at 70% 40%,#2c3340 0%,#161a22 50%,#0b0d12 100%)}
.nav a{color:#fff;text-decoration:none;position:absolute;white-space:nowrap;font-size:15.5px}
.hero-title{left:120px;top:205px;font-size:51px;line-height:54px;width:560px}
.hero-sub{left:122px;top:381px;font-size:15.5px;line-height:22px;width:400px;color:#e8e8e8}

/* about */
.about-card{left:122px;top:717px;width:956px;height:449px;background:var(--panel)}
.about-photo{left:0;top:754px;width:550px;height:375px;background:radial-gradient(ellipse at 50% 45%,#8a6a48 0%,#4a3724 35%,#1d1a18 75%)}
.about-text{left:641px;top:774px;width:355px}
.about-text h2{font-size:31px;line-height:37px;margin-top:12px}
.about-text p{font-size:15px;line-height:22.5px;color:var(--muted);margin-top:24px}
.about-text p span{color:var(--orange)}

/* shop */
.center{left:0;width:1200px;text-align:center}
.section-title{font-size:31px}
.card{top:1367px;width:180px;height:223px;border:1.5px solid var(--orange);border-radius:3px;overflow:hidden;background:#101216}
.card .img{height:178px}
.card .name{font-size:13px;color:var(--blue);text-align:center;margin-top:5px}
.card .price{font-size:11px;color:#fff;text-align:center;margin-top:2px}
.arrow{width:37px;height:37px;border-radius:50%;border:1.5px solid #fff;background:#0e1117;display:flex;align-items:center;justify-content:center}

/* why */
.why{left:0;top:1786px;width:1200px;height:579px;background:var(--panel-2)}
.why-photo{left:642px;top:1786px;width:558px;height:579px;background:linear-gradient(135deg,#6b5a4e 0%,#5b2e18 35%,#3a1e10 65%,#1a1210 100%)}
.feature{left:120px;width:440px}
.feature h3{font-family:'Belleza',sans-serif;font-weight:400;font-size:14px;text-transform:uppercase;display:flex;align-items:center;gap:12px;letter-spacing:.2px}
.feature .ico{width:32px;height:28px;display:flex;align-items:center;justify-content:center}
.feature p{font-size:13px;line-height:20px;color:var(--muted);margin-top:10px}

/* testimonials */
.quote{left:288px;top:2578px;width:624px;font-size:15px;line-height:24px;color:var(--muted);text-align:center}

/* cta */
.cta{left:0;top:2853px;width:1200px;height:400px;background:radial-gradient(ellipse at 35% 30%,#5a4230 0%,#3a2a1f 35%,#1f1814 70%,#15110f 100%)}

/* footer */
.footer-head{font-family:'Belleza',sans-serif;font-size:18px}
.footer-head::after{content:"";display:block;width:90px;height:1.5px;margin-top:10px;background:linear-gradient(90deg,transparent,var(--blue),transparent)}
.flink{font-size:15px;color:var(--muted);position:absolute;left:558px}
.contact-row{left:772px;display:flex;gap:14px;font-size:15px;color:var(--muted);line-height:24px;width:240px}
</style>
</head>
<body>

<!-- Hero -->
<section class="hero-bg abs" role="img" aria-label="Dim dining room with a wooden table, dark upholstered chairs and a stool"></section>
<div class="brand abs" style="left:122px;top:32px"><span class="dot"></span>Heartwood Tables</div>
<nav class="nav abs" style="left:0;top:48px">
  <a style="left:554px">Home</a>
  <a style="left:631px">About Us</a>
  <a style="left:731px">Products</a>
  <a style="left:830px">Testimonials</a>
  <a style="left:953px">Contact</a>
</nav>
<svg class="abs" style="left:1056px;top:49px" width="20" height="20" viewBox="0 0 20 20" fill="none" stroke="#fff" stroke-width="1.6"><path d="M4 7h12l-1 11H5z"/><path d="M7 7V5a3 3 0 0 1 6 0v2"/><circle cx="16" cy="4" r="2.5" fill="#f0692c" stroke="none"/></svg>
<h1 class="display abs hero-title">Discover Timeless Elegance in Sustainable Luxury Furniture</h1>
<p class="abs hero-sub">Experience the Artistry of Nature Transformed into Unparalleled Furniture Creations</p>
<a class="btn btn-fill" style="left:122px;top:454px;width:153px;height:44px">Shop Now</a>

<!-- About -->
<div class="about-card abs"></div>
<div class="about-photo abs" role="img" aria-label="Wooden table with a geometric inlaid top on angular black steel legs"></div>
<div class="about-text abs">
  <div class="eyebrow">About Us</div>
  <h2 class="display">Redefining Luxury with Sustainable Craftsmanship</h2>
  <p>At <span>Heartwood Tables</span>, we redefine the concept of luxury furniture with our unwavering commitment to sustainability and uncompromising craftsmanship. Our exquisite tables and furniture embody timeless elegance and offer a touch of opulence to the discerning clientele who appreciate the finer things in life.</p>
</div>
<a class="btn btn-line" style="left:641px;top:1079px;width:154px;height:45px">Read More</a>

<!-- Featured products -->
<div class="eyebrow abs center" style="top:1280px">Shop</div>
<h2 class="display section-title abs center" style="top:1300px">Featured Products</h2>
<div class="card abs" style="left:122px"><div class="img" role="img" aria-label="Curved slatted wooden lounge chair" style="background:linear-gradient(160deg,#6e5a4c,#3a2418 60%,#1b1512)"></div><div class="name">Lorem ipsum dolor</div><div class="price">$1000.00 - $1599.00</div></div>
<div class="card abs" style="left:316px"><div class="img" role="img" aria-label="Live-edge wooden side table on black legs" style="background:radial-gradient(ellipse at 50% 35%,#7a5a3a,#1a1714 70%)"></div><div class="name">Lorem ipsum dolor</div><div class="price">$1000.00 - $1599.00</div></div>
<div class="card abs" style="left:510px"><div class="img" role="img" aria-label="Wooden armchair with a cream cushion" style="background:linear-gradient(180deg,#5f5b56,#8a7e70 50%,#3e3a35)"></div><div class="name">Lorem ipsum dolor</div><div class="price">$1000.00 - $1599.00</div></div>
<div class="card abs" style="left:705px"><div class="img" role="img" aria-label="Pale wood slab coffee table on dark legs" style="background:linear-gradient(180deg,#d8cfc6,#bfa99a 45%,#2a2420)"></div><div class="name">Lorem ipsum dolor</div><div class="price">$1000.00 - $1599.00</div></div>
<div class="card abs" style="left:899px"><div class="img" role="img" aria-label="Brown leather channel-tufted lounge chair" style="background:radial-gradient(ellipse at 50% 50%,#8a4a28,#2a1a12 75%)"></div><div class="name">Lorem ipsum dolor</div><div class="price">$1000.00 - $1599.00</div></div>
<div class="arrow abs" style="left:102px;top:1459px"><svg width="10" height="10" viewBox="0 0 10 10" fill="none" stroke="#fff" stroke-width="1.6"><path d="M6.5 1.5 3 5l3.5 3.5"/></svg></div>
<div class="arrow abs" style="left:1059px;top:1459px"><svg width="10" height="10" viewBox="0 0 10 10" fill="none" stroke="#fff" stroke-width="1.6"><path d="M3.5 1.5 7 5 3.5 8.5"/></svg></div>
<a class="btn btn-fill" style="left:523px;top:1628px;width:153px;height:45px">Shop Now</a>

<!-- Why us -->
<div class="why abs"></div>
<div class="why-photo abs" role="img" aria-label="Dark wood kitchen stool and woven wicker basket beside a cabinet"></div>
<div class="eyebrow abs" style="left:122px;top:1845px">Why Us</div>
<h2 class="display section-title abs" style="left:122px;top:1866px">Sustainable Luxury Redefined</h2>
<div class="feature abs" style="top:1936px"><h3><span class="ico"><svg width="26" height="24" viewBox="0 0 26 24" fill="none" stroke="#f0692c" stroke-width="1.8"><path d="M13 3 8 9h10z"/><path d="M2 20h8l4-3h9" stroke="#fff"/></svg></span>Sustainable Excellence</h3><p>We prioritize nature by using dead trees for furniture, promoting ecological harmony and sustainability while providing luxurious options.</p></div>
<div class="feature abs" style="top:2030px"><h3><span class="ico"><svg width="24" height="26" viewBox="0 0 24 26" fill="none" stroke="#f0692c" stroke-width="1.8"><circle cx="12" cy="10" r="7"/><path d="M9 19v5M15 19v5" stroke="#fff"/></svg></span>Impeccable Craftsmanship</h3><p>Our experienced and passionate artisans use the finest techniques and tools to meticulously craft furniture with unparalleled quality.</p></div>
<div class="feature abs" style="top:2124px"><h3><span class="ico"><svg width="26" height="26" viewBox="0 0 26 26" fill="none" stroke-width="1.8"><rect x="3" y="9" width="14" height="14" stroke="#fff"/><rect x="10" y="3" width="13" height="13" stroke="#f0692c"/></svg></span>Exceptional Materials</h3><p>We choose superior lumber that's harvested, milled, and kiln-dried, enhancing its natural beauty to produce charming furniture.</p></div>
<div class="feature abs" style="top:2218px"><h3><span class="ico"><svg width="28" height="24" viewBox="0 0 28 24" fill="none" stroke-width="1.8"><rect x="3" y="4" width="22" height="10" rx="3" fill="#f0692c" stroke="none"/><path d="M6 14v7M22 14v7M3 17h22" stroke="#fff"/></svg></span>Unparalleled Design</h3><p>Our furniture designs blend classic elegance and modern aesthetics, with styles ranging from minimalistic to ornate detailing to suit diverse tastes and interiors.</p></div>

<!-- Testimonials -->
<div class="eyebrow abs center" style="top:2454px">Testimonials</div>
<h2 class="display section-title abs center" style="top:2474px">What Our Client Say</h2>
<svg class="abs" style="left:556px;top:2549px" width="88" height="16" viewBox="0 0 88 16" fill="#f0692c"><g id="star"><path d="M8 1l2.1 4.6 5 .5-3.8 3.3 1.1 4.9L8 11.8 3.6 14.3l1.1-4.9L.9 6.1l5-.5z"/></g><use href="#star" x="18"/><use href="#star" x="36"/><use href="#star" x="54"/><use href="#star" x="72"/></svg>
<p class="quote abs">Lorem ipsum dolor sit amet consectetur. Morbi et turpis eget ac cras sit curabitur. Ut consequat proin eget nam nunc massa pharetra pharetra gravida. Nunc adipiscing sit in ut at duis turpis felis velit. Nulla dui posuere eget orci tellus metus scelerisque aliquet gravida. Id porttitor donec et est.</p>
<div class="abs" role="img" aria-label="Client portrait" style="left:515px;top:2690px;width:36px;height:36px;border-radius:50%;border:2px solid var(--blue);background:#c8ccd4"></div>
<div class="abs" style="left:564px;top:2699px;font-size:15px;font-weight:600">Maren Holloway</div>
<svg class="abs" style="left:570px;top:2766px" width="60" height="16" viewBox="0 0 60 16"><circle cx="9" cy="8" r="7" fill="none" stroke="#f0692c" stroke-width="1.3"/><circle cx="9" cy="8" r="3" fill="#f0692c"/><circle cx="28" cy="8" r="2.5" fill="#fff"/><circle cx="40" cy="8" r="2.5" fill="#fff"/><circle cx="52" cy="8" r="2.5" fill="#fff"/></svg>
<div class="arrow abs" style="left:136px;top:2595px"><svg width="10" height="10" viewBox="0 0 10 10" fill="none" stroke="#fff" stroke-width="1.6"><path d="M6.5 1.5 3 5l3.5 3.5"/></svg></div>
<div class="arrow abs" style="left:1017px;top:2595px"><svg width="10" height="10" viewBox="0 0 10 10" fill="none" stroke="#fff" stroke-width="1.6"><path d="M3.5 1.5 7 5 3.5 8.5"/></svg></div>

<!-- CTA -->
<div class="cta abs" role="img" aria-label="Warm-lit wooden table with bowls and a glowing lamp"></div>
<div class="abs center" style="top:2930px;font-size:15px;color:#c4763e">PRODUCTS</div>
<h2 class="display abs center" style="top:2952px;font-size:50px;line-height:54px">Immerse Yourself In<br>Sustainable Luxury</h2>
<p class="abs center" style="top:3077px;font-size:13.5px;line-height:20px;color:#e6e6e6">Explore our Captivating Collection and Elevate Your Living<br>Spaces Today!</p>
<a class="btn btn-fill" style="left:523px;top:3132px;width:153px;height:45px">Shop Now</a>

<!-- Footer -->
<footer>
  <div class="brand abs" style="left:125px;top:3316px"><span class="dot"></span>Heartwood Tables</div>
  <div class="abs" style="left:149px;top:3382px;font-size:17px">FOLLOW US</div>
  <svg class="abs" style="left:149px;top:3414px" width="90" height="20" viewBox="0 0 90 20" fill="none" stroke="#f0692c" stroke-width="1.6"><circle cx="9" cy="10" r="7.5"/><circle cx="42" cy="10" r="7.5"/><circle cx="75" cy="10" r="7.5"/></svg>

  <div class="footer-head abs" style="left:554px;top:3306px">QUICK LINKS</div>
  <span class="flink" style="top:3365px">Home</span>
  <span class="flink" style="top:3394px">About Us</span>
  <span class="flink" style="top:3423px">Products</span>
  <span class="flink" style="top:3452px">Testimonials</span>
  <span class="flink" style="top:3481px">Contact</span>

  <div class="footer-head abs" style="left:772px;top:3307px">CONTACT</div>
  <div class="contact-row abs" style="top:3368px"><svg width="14" height="18" viewBox="0 0 14 18" style="flex:none;margin-top:2px"><path d="M7 0a6 6 0 0 1 6 6c0 4.5-6 12-6 12S1 10.5 1 6a6 6 0 0 1 6-6z" fill="#f0692c"/><circle cx="7" cy="6" r="2.2" fill="#0e1117"/></svg><span>418 Cedar Hollow Rd. Ashgrove, Oregon 97012</span></div>
  <div class="contact-row abs" style="top:3421px"><svg width="14" height="16" viewBox="0 0 14 16" style="flex:none;margin-top:3px"><path d="M2 1h3l1.5 4-2 1.3a9 9 0 0 0 4.2 4.2L10 8.5l4 1.5v3a2 2 0 0 1-2 2A12 12 0 0 1 0 3a2 2 0 0 1 2-2z" fill="#f0692c"/></svg><span>(541) 555-0187</span></div>
  <div class="contact-row abs" style="top:3453px"><svg width="14" height="12" viewBox="0 0 14 12" style="flex:none;margin-top:6px"><rect width="14" height="11" rx="1.5" fill="#f0692c"/><path d="M1 1.5 7 6l6-4.5" stroke="#0e1117" stroke-width="1.3" fill="none"/></svg><span>hello@heartwoodtables.example</span></div>

  <div class="abs" style="left:120px;top:3549px;width:960px;height:1px;background:var(--line)"></div>
  <div class="abs center" style="top:3590px;font-size:12.5px;color:var(--muted)">Copyright Heartwood Tables | All rights reserved</div>
</footer>

</body>
</html>
```